Velta Harbor Solutions

I have a file with a logo. It is grainy. I also have a board with my color pallet and other branding items. I need a file with the logo that is high resolution and I also need a business card design.

```html
<!DOCTYPE html>
<html lang="en">
<head>
<meta charset="utf-8">
<title>Velta Harbor Solutions — Business Card</title>
<link rel="stylesheet" href="https://fonts.googleapis.com/css2?family=Montserrat:wght@400;500;600;700&display=swap">
<style>
  :root {
    --stage: #3b3c3e;
    --navy: #222938;
    --white: #ffffff;
    --red: #a8282b;
    --rule: #6b7384;
    --ink: #222938;
  }
  * { margin: 0; padding: 0; box-sizing: border-box; }
  html, body { width: 1200px; height: 1200px; overflow: hidden; }
  body {
    background: var(--stage);
    font-family: "Montserrat", sans-serif;
    position: relative;
  }
  .card {
    position: absolute;
    left: 180px;
    width: 840px;
    height: 480px;
    border-radius: 38px;
    overflow: hidden;
    box-shadow: 0 14px 30px rgba(0,0,0,0.35);
  }
  .card--front { top: 80px; background: var(--white); }
  .card--back { top: 640px; background: var(--navy); }

  /* front */
  .front__brand-area {
    position: absolute; left: 0; top: 0; width: 100%; height: 250px;
    display: flex; align-items: center; justify-content: center;
  }
  .brand-name {
    font-weight: 700;
    font-size: 34px;
    letter-spacing: 1px;
    display: flex; align-items: center; gap: 16px;
  }
  .brand-name__mark { width: 18px; height: 18px; background: var(--red); }
  .front__brand-area .brand-name { color: var(--ink); }

  .front__red-rule {
    position: absolute; left: 0; top: 262px; width: 100%; height: 6px; background: var(--red);
  }
  .front__band {
    position: absolute; left: 0; top: 276px; width: 100%; height: 204px; background: var(--navy);
  }
  .identity {
    position: absolute; left: 80px; top: 60px;
  }
  .identity__name {
    color: var(--red); font-weight: 600; font-size: 36px; letter-spacing: 0.5px; line-height: 1.1;
  }
  .identity__title {
    color: var(--white); font-weight: 400; font-size: 24px; margin-top: 4px;
  }
  .band__divider {
    position: absolute; left: 420px; top: 36px; width: 1px; height: 132px; background: var(--rule);
  }
  .contact {
    position: absolute; left: 460px; top: 40px; list-style: none;
  }
  .contact__item {
    display: flex; align-items: center; gap: 12px;
    color: var(--white); font-size: 22px; font-weight: 400; height: 42px;
  }
  .contact__icon { width: 22px; height: 22px; flex: none; }

  /* back */
  .card--back .brand-name {
    position: absolute; inset: 0; justify-content: center;
    color: var(--white); font-size: 44px;
  }
  .card--back .brand-name__mark { width: 22px; height: 22px; }
</style>
</head>
<body>

<section class="card card--front" aria-label="Business card front">
  <div class="front__brand-area">
    <div class="brand-name"><span class="brand-name__mark"></span>Velta Harbor Solutions</div>
  </div>
  <div class="front__red-rule"></div>
  <div class="front__band">
    <div class="identity">
      <p class="identity__name">FULL NAME</p>
      <p class="identity__title">TITLE</p>
    </div>
    <div class="band__divider"></div>
    <ul class="contact">
      <li class="contact__item">
        <svg class="contact__icon" viewBox="0 0 24 24" aria-hidden="true"><path fill="#a8282b" d="M6.6 10.8a15 15 0 0 0 6.6 6.6l2.2-2.2c.3-.3.7-.4 1-.2 1.1.4 2.3.6 3.6.6.6 0 1 .4 1 1V20c0 .6-.4 1-1 1A17 17 0 0 1 3 4c0-.6.4-1 1-1h3.5c.6 0 1 .4 1 1 0 1.3.2 2.5.6 3.6.1.3 0 .7-.2 1z"/></svg>
        (000) 000 0000
      </li>
      <li class="contact__item">
        <svg class="contact__icon" viewBox="0 0 24 24" aria-hidden="true"><rect x="2" y="5" width="20" height="14" rx="1.5" fill="#a8282b"/><path d="M3 6l9 7 9-7" fill="none" stroke="#222938" stroke-width="1.6"/></svg>
        email@company.com
      </li>
      <li class="contact__item">
        <svg class="contact__icon" viewBox="0 0 24 24" aria-hidden="true"><g fill="none" stroke="#a8282b" stroke-width="1.8"><circle cx="12" cy="12" r="9.5"/><ellipse cx="12" cy="12" rx="4.2" ry="9.5"/><path d="M2.5 12h19M4 7h16M4 17h16"/></g></svg>
        www.company.com
      </li>
    </ul>
  </div>
</section>

<section class="card card--back" aria-label="Business card back">
  <div class="brand-name"><span class="brand-name__mark"></span>Velta Harbor Solutions</div>
</section>

</body>
</html>
```